Milo Castell Moving DL Flyer

We need a double sided DL flyer to give to patients to let them know that we are moving location.
On one side we would like it to read:
"We Are Moving!" and "November 2017" and our logo.
On the other side we would like it to read:
"Same Great Staff"
"Same Great Service"
"Bigger, Brighter and Better"
"New Location at 42 Quarry Rd"
with a map below (attached)
The flyer should follow our practice branding. Attached is a copy of our business card as an example of this.

```html
<!DOCTYPE html>
<html lang="en">
<head>
<meta charset="utf-8">
<title>Milo Castell Optometry – Moving Flyer</title>
<link href="https://fonts.googleapis.com/css2?family=Montserrat:wght@500;600;700&family=Kalam:wght@700&display=swap" rel="stylesheet">
<style>
  :root {
    --plum: #4f3b58;
    --plum-dark: #433249;
    --ink: #1d1d1f;
    --paper: #ffffff;
    --backdrop: #e6e4e7;
    --map-tone: #b9b3bd;
  }
  * { box-sizing: border-box; margin: 0; padding: 0; }
  html, body { width: 1098px; height: 1200px; overflow: hidden; }
  body {
    background: var(--backdrop);
    font-family: "Montserrat", Arial, sans-serif;
    position: relative;
  }
  .flyer-side {
    position: absolute;
    left: 104px;
    width: 892px;
    height: 420px;
    background: var(--paper);
    overflow: hidden;
    box-shadow: 0 6px 18px rgba(0,0,0,.18);
  }
  .flyer-front { top: 160px; }
  .flyer-back { top: 620px; }
  .edge-band { position: absolute; top: 0; right: 0; height: 420px; }

  .brand-name {
    position: absolute;
    color: var(--ink);
    font-weight: 600;
    line-height: 1.05;
    display: flex;
    align-items: center;
    gap: 10px;
  }
  .brand-name .brand-square {
    width: 14px; height: 14px; background: var(--plum); flex: none;
  }
  .flyer-front .brand-name { left: 168px; top: 44px; font-size: 22px; }

  .headline-top {
    position: absolute; left: 124px; top: 128px;
    font-size: 66px; font-weight: 700; color: var(--plum); letter-spacing: 1px;
  }
  .headline-main {
    position: absolute; left: 40px; top: 200px;
    font-size: 94px; font-weight: 700; color: var(--ink); letter-spacing: 1px;
  }
  .date-pill {
    position: absolute; left: 94px; top: 326px;
    width: 362px; height: 58px; border-radius: 29px;
    background: var(--plum); color: var(--paper);
    font-size: 32px; font-weight: 600; letter-spacing: 1px;
    display: flex; align-items: center; justify-content: center;
  }

  .promise {
    position: absolute; left: 40px;
    font-family: "Kalam", cursive; color: var(--plum);
  }
  .promise .promise-lead {
    display: block; font-family: "Montserrat", sans-serif;
    font-size: 15px; font-weight: 600; margin-left: 52px; line-height: 1;
  }
  .promise .promise-text { display: block; font-size: 46px; line-height: 1; }
  .promise-staff { top: 36px; }
  .promise-service { top: 126px; }
  .promise-divider {
    position: absolute; left: 40px; top: 114px;
    width: 310px; height: 3px; background: var(--plum);
  }

  .upgrade-list {
    position: absolute; left: 36px; top: 210px;
    list-style: none; color: var(--ink);
    font-size: 27px; font-weight: 600; line-height: 33px;
  }
  .upgrade-list li { display: flex; align-items: center; gap: 10px; }
  .upgrade-list svg { flex: none; }

  .flyer-back .brand-name { left: 232px; top: 234px; font-size: 24px; }

  .address-pill {
    position: absolute; left: 0; top: 338px;
    width: 396px; height: 44px; border-radius: 0 22px 22px 0;
    background: var(--plum); color: var(--paper);
    font-size: 20px; font-weight: 600; padding-left: 44px;
    display: flex; align-items: center;
  }

  .location-map {
    position: absolute; left: 466px; top: 24px;
    width: 372px; height: 374px;
    background: linear-gradient(135deg, #c3bec6 0%, var(--map-tone) 55%, #e9a3a3 100%);
  }
</style>
</head>
<body>

  <section class="flyer-side flyer-front">
    <svg class="edge-band" width="260" height="420" viewBox="0 0 260 420" aria-hidden="true">
      <path d="M150 0 H260 V420 H96 C140 300 160 150 150 0 Z" fill="var(--plum)"/>
      <path d="M118 0 C132 150 116 300 70 420" fill="none" stroke="var(--plum)" stroke-width="10"/>
    </svg>
    <div class="brand-name"><span class="brand-square"></span>Milo Castell Optometry</div>
    <h1 class="headline-top">WE ARE</h1>
    <p class="headline-main">MOVING!</p>
    <div class="date-pill">NOVEMBER 2017</div>
  </section>

  <section class="flyer-side flyer-back">
    <svg class="edge-band" width="200" height="420" viewBox="0 0 200 420" aria-hidden="true">
      <path d="M110 0 H200 V420 H90 C104 280 112 140 110 0 Z" fill="var(--plum)"/>
      <path d="M76 0 C84 140 80 280 64 420" fill="none" stroke="var(--plum)" stroke-width="8"/>
    </svg>

    <div class="promise promise-staff">
      <span class="promise-lead">Same</span>
      <span class="promise-text">Great Staff</span>
    </div>
    <div class="promise-divider"></div>
    <div class="promise promise-service">
      <span class="promise-lead">Same</span>
      <span class="promise-text">Great Service</span>
    </div>

    <ul class="upgrade-list">
      <li><svg width="20" height="20" viewBox="0 0 20 20" aria-hidden="true"><path d="M2 11 L8 17 L18 3" fill="none" stroke="var(--ink)" stroke-width="3" stroke-linecap="round" stroke-linejoin="round"/></svg>Bigger</li>
      <li><svg width="20" height="20" viewBox="0 0 20 20" aria-hidden="true"><path d="M2 11 L8 17 L18 3" fill="none" stroke="var(--ink)" stroke-width="3" stroke-linecap="round" stroke-linejoin="round"/></svg>Brighter</li>
      <li><svg width="20" height="20" viewBox="0 0 20 20" aria-hidden="true"><path d="M2 11 L8 17 L18 3" fill="none" stroke="var(--ink)" stroke-width="3" stroke-linecap="round" stroke-linejoin="round"/></svg>&amp; Better</li>
    </ul>

    <div class="brand-name"><span class="brand-square"></span>Milo Castell<br>Optometry</div>

    <div class="address-pill">New Location at 42 Quarry Rd</div>

    <div class="location-map" role="img" aria-label="Street map showing the new practice location beside the marketplace, with surrounding streets, car parking and neighbouring shops"></div>
  </section>

</body>
</html>
```